International Business Consulting Company Website

RV Crestline Advisory is a U.S-based international consulting firm. We combined passion for success in the global business arena with hands-on experience to help foreign companies navigate the entry into U.S. markets and U.S. companies in initiating and expanding exports to foreign markets.

We need a simple 1 page website
Examples of other consultants’ websites:
http://www.falconridgeadvisors.example/#intro
https://www.mtq-advisers.example
http://veronagroup.example
https://harborwiseadvisory.example

I also need the designer to suggest stock images that are suitable (related to international business, exports).

We want our web design to be bold, yet clean and simple.

Target Market(s)

US companies that export abroad, foreign companies that want to do business int he US/ open a subsidiary in the US.

Industry/Entity Type

Business Consultant

Coding

Coded - Design and coding required

Font styles to use
Sans Serif

Requirements
Must have
• Company logo on top

```html
<!DOCTYPE html>
<html lang="en">
<head>
<meta charset="utf-8">
<title>RV Crestline Advisory – International Consulting Firm</title>
<link href="https://fonts.googleapis.com/css2?family=Montserrat:wght@400;600;700;800&family=Open+Sans:wght@400;600;700&display=swap" rel="stylesheet">
<style>
:root{
  --navy:#0b2554;
  --navy-deep:#071a3d;
  --blue:#1560bd;
  --blue-bright:#2b86dc;
  --sky:#5fa8ea;
  --grey-bg:#e8ecf1;
  --text:#3d4450;
  --text-soft:#6a7280;
  --white:#ffffff;
}
*{margin:0;padding:0;box-sizing:border-box}
html,body{width:1200px;height:3236px;overflow:hidden}
body{font-family:"Open Sans",Arial,sans-serif;color:var(--text);background:var(--white)}
section,header,footer{position:relative;width:1200px;overflow:hidden}

/* Hero */
.hero{height:790px}
.hero-photo{position:absolute;inset:0;background:linear-gradient(180deg,#123a78 0%,#2d6fc0 35%,#6aa6df 55%,#1d4f93 75%,#0c2b5c 100%)}
.nav{position:absolute;top:0;left:0;right:0;height:70px;background:rgba(7,26,61,.85);display:flex;align-items:center;justify-content:space-between;padding:0 40px}
.brand{display:flex;align-items:center;gap:10px;font-family:"Montserrat",sans-serif;font-weight:700;color:var(--white);font-size:17px;letter-spacing:1px;white-space:nowrap}
.brand-square{width:30px;height:30px;border:2px solid var(--white)}
.menu{display:flex;gap:34px;align-items:center;font-family:"Montserrat",sans-serif;font-size:14px;font-weight:600;color:var(--white)}
.hero-logo{position:absolute;left:430px;top:350px;width:340px;height:164px;background:rgba(255,255,255,.95);display:flex;flex-direction:column;align-items:center;justify-content:center;gap:14px}
.hero-logo .mark{width:44px;height:44px;border:4px solid var(--navy)}
.hero-logo .name{font-family:"Montserrat",sans-serif;font-weight:700;color:var(--navy);font-size:26px;letter-spacing:1px;text-align:center;line-height:1.15}
.hero-tag{position:absolute;left:430px;top:522px;width:340px;height:42px;background:var(--navy);color:var(--white);font-family:"Montserrat",sans-serif;font-weight:600;font-size:15px;letter-spacing:.5px;white-space:nowrap;display:flex;align-items:center;justify-content:center}

/* Intro */
.intro{height:150px;text-align:center;padding-top:26px}
.intro h1{font-family:"Montserrat",sans-serif;font-weight:700;font-size:22px;color:var(--text);margin-bottom:14px}
.intro p{width:780px;margin:0 auto;font-size:16px;font-weight:700;color:var(--text-soft);line-height:1.45}

/* Section bands */
.band{display:flex;align-items:center;justify-content:center;gap:26px;background:linear-gradient(90deg,var(--navy) 0%,var(--blue) 50%,var(--navy) 100%)}
.band h2{font-family:"Montserrat",sans-serif;font-weight:800;font-size:62px;color:var(--white);letter-spacing:1px}
.services-band{height:180px}
.about-band{height:210px;padding-bottom:40px}

/* Services */
.services{height:580px;background:var(--grey-bg)}
.service-card{position:absolute;background:var(--white);padding:30px 40px;box-shadow:0 4px 14px rgba(0,0,0,.12)}
.service-card h3{font-family:"Montserrat",sans-serif;font-weight:800;font-size:42px;line-height:1.05;color:var(--navy)}
.service-card p{font-family:"Montserrat",sans-serif;font-weight:700;font-size:16px;color:var(--blue);margin-top:10px;line-height:1.35}
.card-exports{left:100px;top:80px;width:520px;height:210px}
.card-fdi{left:620px;top:330px;width:520px;height:200px}
.service-list{position:absolute;list-style:none;font-size:13px;line-height:1.5;color:var(--text)}
.service-list li{position:relative;padding-left:20px;margin-bottom:9px}
.service-list li::before{content:"";position:absolute;left:2px;top:6px;width:8px;height:8px;background:var(--blue-bright)}
.list-exports{left:660px;top:70px;width:460px}
.list-fdi{left:110px;top:350px;width:460px}

/* About */
.bio{height:660px}
.portrait{position:absolute;left:496px;top:-60px;width:208px;height:208px;border-radius:50%;border:6px solid var(--white);background:radial-gradient(circle at 50% 40%,#c9b8a8 0%,#8c7766 55%,#4c4a55 100%)}
.bio-text{position:absolute;left:100px;top:180px;width:1000px;font-size:14px;line-height:1.65;color:var(--text)}
.bio-text p{margin-bottom:20px}
.bio-text .lead{font-weight:700}
.bio-text .languages{text-align:center;font-weight:700;font-style:italic;color:var(--blue)}

/* Contact */
.contact{height:610px;background:radial-gradient(ellipse at 50% 40%,#1a4f9a 0%,var(--navy) 60%,var(--navy-deep) 100%)}
.contact-brand{position:absolute;top:56px;left:0;right:0;display:flex;justify-content:center}
.contact-brand .brand{font-size:26px}
.contact-brand .brand-square{width:40px;height:40px}
.laptop-screen{position:absolute;left:400px;top:170px;width:500px;height:360px;background:var(--white);border:16px solid #1c1f26;border-radius:14px 14px 0 0;text-align:center}
.laptop-base{position:absolute;left:370px;top:530px;width:560px;height:22px;background:linear-gradient(180deg,#cfd4da,#8d949c);border-radius:0 0 18px 18px}
.screen-title{margin-top:22px;height:48px;background:var(--blue);color:var(--white);font-family:"Montserrat",sans-serif;font-weight:700;font-size:26px;display:flex;align-items:center;justify-content:center}
.contact-name{margin-top:22px;font-family:"Montserrat",sans-serif;font-weight:800;font-size:28px;color:var(--navy);white-space:nowrap}
.contact-role{margin:10px auto 0;width:200px;height:30px;background:var(--navy);color:var(--white);font-family:"Montserrat",sans-serif;font-weight:600;font-size:15px;letter-spacing:2px;display:flex;align-items:center;justify-content:center}
.contact-line{display:flex;align-items:center;justify-content:center;gap:12px;margin-top:22px;font-size:17px;font-weight:600;color:var(--text);white-space:nowrap}
.scroll-down{position:absolute;left:1048px;top:550px;width:48px;height:48px;border-radius:50%;background:var(--white);display:flex;align-items:center;justify-content:center}

/* Footer */
.footer{height:56px;background:var(--white);display:flex;align-items:center;justify-content:center;font-size:12px;font-weight:600;color:var(--text-soft);letter-spacing:.5px}
</style>
</head>
<body>

<header class="hero">
  <div class="hero-photo" role="img" aria-label="Cargo ship stacked with shipping containers at sea with a cargo plane overhead, in deep blue tones"></div>
  <nav class="nav">
    <div class="brand"><span class="brand-square"></span>RV CRESTLINE ADVISORY</div>
    <div class="menu">
      <span>HOME</span><span>OUR SERVICES</span><span>ABOUT US</span><span>CONTACT US</span>
      <svg width="16" height="16" viewBox="0 0 16 16" fill="none" stroke="#fff" stroke-width="2"><circle cx="6.5" cy="6.5" r="5"/><line x1="10.5" y1="10.5" x2="15" y2="15"/></svg>
    </div>
  </nav>
  <div class="hero-logo">
    <span class="mark"></span>
    <div class="name">RV CRESTLINE<br>ADVISORY</div>
  </div>
  <div class="hero-tag">INTERNATIONAL CONSULTING FIRM</div>
</header>

<section class="intro">
  <h1>RV Crestline Advisory</h1>
  <p>is a U.S-based international consulting firm. We combined passion for success in the global business arena with hands-on experience to help foreign companies navigate the entry into U.S. markets and U.S. companies in initiating and expanding exports to foreign markets.</p>
</section>

<section class="band services-band">
  <svg width="74" height="64" viewBox="0 0 74 64" fill="none" stroke="#fff" stroke-width="3" stroke-linecap="round" stroke-linejoin="round">
    <circle cx="44" cy="18" r="14"/>
    <path d="M40 12h8M44 8v20M40 24h8"/>
    <path d="M4 46h12l10 6h22a4 4 0 0 0 0-8H34"/>
    <path d="M16 40l12-4h8l22-6a4 4 0 0 1 3 7L40 58H20L4 54"/>
  </svg>
  <h2>OUR SERVICES</h2>
</section>

<section class="services">
  <div class="service-card card-exports">
    <h3>RV CRESTLINE ADVISORY</h3>
    <p>EXPORTS ASSISTS U.S. COMPANIES WITH THEIR EXPORT INITIATIVES BY</p>
  </div>
  <ul class="service-list list-exports">
    <li>Identifying and developing new customer relationships in foreign markets</li>
    <li>Organizing trade mission trips</li>
    <li>Coordinating successful trade show visits</li>
    <li>Providing an assistance with the completion of a strategic export plan</li>
    <li>Finding additional resources to support and grow companies' exports</li>
    <li>Connecting companies with other international trade experts to further support their international logistics, payment &amp; financing management, and to address any trade regulations and legal issues</li>
  </ul>
  <ul class="service-list list-fdi">
    <li>Managing the site selection process</li>
    <li>Collecting market data</li>
    <li>Site identification and analysis</li>
    <li>Providing an operational go-to-market incentives and financing assistance</li>
    <li>Management of the documentation process</li>
  </ul>
  <div class="service-card card-fdi">
    <h3>RV CRESTLINE ADVISORY</h3>
    <p>FDI ASSISTS INTERNATIONAL COMPANIES WITH NAVIGATING THE ENTRY INTO U.S. MARKETS BY</p>
  </div>
</section>

<section class="band about-band">
  <svg width="70" height="70" viewBox="0 0 70 70" fill="none" stroke="#fff" stroke-width="4">
    <circle cx="35" cy="35" r="31"/>
    <circle cx="35" cy="20" r="3" fill="#fff"/>
    <path d="M29 30h7v20M28 50h15" stroke-linecap="round"/>
  </svg>
  <h2>ABOUT US</h2>
</section>

<section class="bio">
  <div class="portrait" role="img" aria-label="Portrait photograph of the company president"></div>
  <div class="bio-text">
    <p><span class="lead">Mira Castellan</span> has ten years of experience in economic development, foreign direct investment and trade promotion. Before founding RV Crestline Advisory, she directed business development for a state economic office, where she helped companies enter new markets and supported investors opening their first American facilities.</p>
    <p><span class="lead">Mira</span> was appointed to a regional export council, joining business leaders who advise local firms on international sales. She was also recognized as an export champion for her work with small manufacturers.</p>
    <p><span class="lead">Mira</span> serves as an honorary consul for the state, building close ties between both sides of the Atlantic and helping Central European firms find partners in the Midwest.</p>
    <p>Passionate about her community, she has served on several nonprofit boards and organizations, including a regional leadership institute, a women in international trade network and a local arts council.</p>
    <p><span class="lead">Mira</span> holds an MBA from a state university, where she studied international business, and a bachelor's degree in finance. She completed an advanced leadership program in 2014.</p>
    <p class="languages">Mira is fluent in English and Czech. She also speaks German and Slovakian.</p>
  </div>
</section>

<section class="contact">
  <div class="contact-brand"><div class="brand"><span class="brand-square"></span>RV CRESTLINE ADVISORY</div></div>
  <div class="laptop-screen">
    <div class="screen-title">CONTACT US</div>
    <div class="contact-name">MIRA CASTELLAN, MBA</div>
    <div class="contact-role">PRESIDENT</div>
    <div class="contact-line">
      <svg width="26" height="26" viewBox="0 0 26 26"><circle cx="13" cy="13" r="13" fill="#1560bd"/><rect x="6" y="8" width="14" height="10" fill="none" stroke="#fff" stroke-width="1.6"/><path d="M6 8l7 6 7-6" fill="none" stroke="#fff" stroke-width="1.6"/></svg>
      info@RVCrestlineAdvisory.example
    </div>
    <div class="contact-line">
      <svg width="26" height="26" viewBox="0 0 26 26"><circle cx="13" cy="13" r="13" fill="#1560bd"/><path d="M9 6l3 4-2 2c1 2 2 3 4 4l2-2 4 3-2 3c-6 0-12-6-12-12z" fill="#fff"/></svg>
      +1 (555) 014-2276
    </div>
  </div>
  <div class="laptop-base"></div>
  <div class="scroll-down">
    <svg width="20" height="12" viewBox="0 0 20 12" fill="none" stroke="#0b2554" stroke-width="3" stroke-linecap="round" stroke-linejoin="round"><path d="M2 2l8 8 8-8"/></svg>
  </div>
</section>

<footer class="footer">© COPYRIGHT 2017 RV CRESTLINE ADVISORY, LLC ALL RIGHTS RESERVED.</footer>

</body>
</html>
```